Copperfield Roofing Co. business card design

I am a Roofing contractor in Texas. The name of my company is Copperfield Roofing Co. I also offer a few other services (Christmas light installation, gutters, fencing, pressure washing). However my main gig is roofing. Storm restoration and knowledge of the insurance claim process is my specialty.

My colors are black, red and white. I’d like something pretty simple and clean. Modern looking but with a splash of this red tartan pattern.

I have another version of my logo being edited at the moment where the little top part of the F in roofing that’s currently tartan will be changed to just solid red to make it more visible. So if that’s something you can change in your mock up great. But I can provide the full version once the contest is complete

Target Market(s)

Homeowners

Industry/Entity Type

Roofing

Contact Information for Business Card

Derek Pruitt. 682-555-0193. www.copperfield roofing.co Derek@copperfieldroofing.co

Colors
EB3D1F
EC4F4E
F09395
F8D3D4
FCEDEE

Requirements
Nice to have
• Maybe instead of a business address. I could say serving all DFW Texas or something like that. And maybe add a line somewhere saying deductible assistance? Just a thought

```html
<!DOCTYPE html>
<html lang="en">
<head>
<meta charset="utf-8">
<title>Copperfield Roofing Co. — Business Card</title>
<link href="https://fonts.googleapis.com/css2?family=Michroma&family=Poppins:wght@400;500&display=swap" rel="stylesheet">
<style>
  :root {
    --red: #d90a0a;
    --red-deep: #c40606;
    --red-light: #e3221c;
    --black: #111111;
    --white: #ffffff;
    --rule: #9a9a9a;
    --backdrop: #1f1f1f;
  }
  * { box-sizing: border-box; margin: 0; padding: 0; }
  html, body {
    width: 1200px; height: 1108px; overflow: hidden;
    background: var(--backdrop);
  }
  .stage {
    width: 1200px; height: 1108px;
    display: flex; align-items: center; justify-content: center; gap: 80px;
  }
  .card {
    width: 420px; height: 735px;
    border-radius: 26px;
    position: relative; overflow: hidden;
    box-shadow: 0 18px 40px rgba(0,0,0,.55);
  }

  /* Front */
  .card-front {
    background: var(--white);
    display: flex; flex-direction: column; align-items: center;
    padding: 90px 34px 0;
  }
  .brand-mark {
    width: 150px; height: 150px; border-radius: 50%;
    background: var(--red);
  }
  .brand-name {
    margin-top: 34px;
    font-family: "Michroma", sans-serif;
    font-size: 27px; line-height: 1.25; text-align: center;
    color: var(--black); letter-spacing: 1px;
    text-transform: uppercase;
  }
  .person-name {
    margin-top: 62px;
    font-family: "Michroma", sans-serif;
    font-size: 27px; color: var(--red); letter-spacing: 1px;
    text-transform: uppercase;
  }
  .icon-row {
    margin-top: 20px; width: 100%;
    display: flex; align-items: center; gap: 10px;
  }
  .icon-row .rule { flex: 1; height: 1px; background: var(--rule); }
  .icon {
    width: 36px; height: 36px; border-radius: 6px;
    background: var(--red);
    display: flex; align-items: center; justify-content: center;
  }
  .icon svg { width: 22px; height: 22px; }
  .contact {
    margin-top: 16px;
    font-family: "Poppins", sans-serif; font-size: 19px;
    color: var(--black); text-align: center; line-height: 1.45;
  }
  .divider { margin-top: 22px; width: 82%; height: 1px; background: var(--rule); }
  .service-area {
    margin-top: 26px;
    font-family: "Michroma", sans-serif; font-size: 20px;
    color: var(--black); letter-spacing: 1px; text-transform: uppercase;
  }

  /* Back */
  .card-back { background: var(--red); }
  .back-texture {
    position: absolute; inset: 0;
    background: linear-gradient(160deg, var(--red-light) 0%, var(--red) 45%, var(--red-deep) 100%);
  }
  .back-name {
    position: absolute; left: 44px; bottom: 110px;
    font-family: "Michroma", sans-serif; font-size: 26px; line-height: 1.25;
    color: var(--white); letter-spacing: 1px; text-transform: uppercase;
  }
</style>
</head>
<body>
<main class="stage">
  <section class="card card-front">
    <div class="brand-mark" aria-hidden="true"></div>
    <p class="brand-name">Copperfield<br>Roofing Co.</p>
    <h1 class="person-name">Derek Pruitt</h1>
    <div class="icon-row">
      <span class="rule"></span>
      <span class="icon" aria-label="Phone">
        <svg viewBox="0 0 24 24" fill="none" stroke="#fff" stroke-width="2" stroke-linecap="round" stroke-linejoin="round"><path d="M5 4h4l2 5-2.5 1.5a11 11 0 0 0 5 5L15 13l5 2v4a2 2 0 0 1-2 2A16 16 0 0 1 3 6a2 2 0 0 1 2-2"/></svg>
      </span>
      <span class="icon" aria-label="Email">
        <svg viewBox="0 0 24 24" fill="none" stroke="#fff" stroke-width="2" stroke-linejoin="round"><rect x="3" y="5" width="18" height="14" rx="1"/><path d="M3 6l9 7 9-7"/></svg>
      </span>
      <span class="icon" aria-label="Website">
        <svg viewBox="0 0 24 24" fill="none" stroke="#fff" stroke-width="2"><circle cx="12" cy="12" r="9"/><path d="M3 12h18M12 3c3 3 3 15 0 18M12 3c-3 3-3 15 0 18"/></svg>
      </span>
      <span class="rule"></span>
    </div>
    <address class="contact">
      682-555-0193<br>
      Derek@copperfieldroofing.co<br>
      www.copperfieldroofing.co
    </address>
    <div class="divider"></div>
    <p class="service-area">Serving all DFW Texas</p>
  </section>

  <section class="card card-back">
    <div class="back-texture" role="img" aria-label="Embossed repeating company name pattern on red"></div>
    <p class="back-name">Copperfield<br>Roofing Co.</p>
  </section>
</main>
</body>
</html>
```